Appraisal and Umpire Services for Property Damage Insurance Claims

I need a banner design that I can post as an advertisement on industry web pages. I would like this to be elegant and reflective of quality, integrity and professionalism.

Target Market(s)

Insurance Companies and Attorneys

Industry/Entity Type

Insurance

Contact Information for Business Card

Gerald M. Hollis
918 Birchwell Lane
PO Box 582
Clifton Park, NY 12093
ghollis@brindlevault.com
Phone: (800) 555-0147, Ext. 2861
Direct: (315) 555-0189

Logo Text

Line One: Velmar Brook Claim Service, Inc. Line two: Appraisal and Umpire Services

Font styles to use
Serif
Sans Serif

Colors
0255a3
f78f20
faa54b
3176b5

Requirements
Must have
• New Logo and matching banner, business card and stationary.
• The colors must be orange and navy blue in the logo. I have selected them below.

```html
<!DOCTYPE html>
<html lang="en">
<head>
<meta charset="utf-8">
<title>Velmar Brook Claim Service – Banner Set</title>
<link rel="stylesheet" href="https://fonts.googleapis.com/css2?family=Open+Sans:wght@300;400;700&family=Fira+Sans+Extra+Condensed:wght@700&display=swap">
<style>
  :root {
    --navy: #0255a3;
    --orange: #f78f20;
    --orange-deep: #f56f0a;
    --white: #ffffff;
    --stage: #000000;
  }
  html, body {
    margin: 0;
    width: 1200px;
    height: 1200px;
    overflow: hidden;
    background: var(--stage);
  }
  .banner {
    position: absolute;
    left: 84px;
    width: 1037px;
    height: 218px;
    display: block;
  }
  .banner--storm { top: 184px; }
  .banner--fire { top: 482px; }
  .banner--tornado { top: 791px; }
  .brand-name { font-family: "Open Sans", sans-serif; font-weight: 700; font-size: 52px; fill: var(--white); }
  .brand-line { font-family: "Open Sans", sans-serif; font-weight: 300; font-size: 53px; fill: var(--white); }
  .contact-head { font-family: "Open Sans", sans-serif; font-weight: 700; font-size: 21px; fill: var(--white); }
  .contact-line { font-family: "Open Sans", sans-serif; font-weight: 300; font-size: 21px; fill: var(--white); }
  .tagline {
    font-family: "Fira Sans Extra Condensed", sans-serif;
    font-weight: 700;
    font-size: 54px;
    fill: var(--orange-deep);
    stroke: var(--white);
    stroke-width: 3px;
    paint-order: stroke;
  }
  .panel { fill: var(--navy); }
  .stripe { fill: var(--orange-deep); }
  .logo-square { fill: var(--orange-deep); }
</style>
</head>
<body>

<svg class="banner banner--storm" viewBox="0 0 1296 272" xmlns="http://www.w3.org/2000/svg">
  <defs>
    <clipPath id="clip-storm"><polygon points="657,0 1296,0 1296,272 460,272"/></clipPath>
    <linearGradient id="storm-base" x1="0" y1="0" x2="0" y2="1">
      <stop offset="0" stop-color="#a7aab3"/>
      <stop offset="0.18" stop-color="#8d8e95"/>
      <stop offset="0.32" stop-color="#4f4c4a"/>
      <stop offset="0.55" stop-color="#6e5d47"/>
      <stop offset="0.8" stop-color="#9a7f60"/>
      <stop offset="1" stop-color="#4a3d32"/>
    </linearGradient>
    <radialGradient id="storm-house" cx="0.2" cy="0.5" r="0.25">
      <stop offset="0" stop-color="#b9d6b0" stop-opacity="0.85"/>
      <stop offset="1" stop-color="#b9d6b0" stop-opacity="0"/>
    </radialGradient>
    <radialGradient id="storm-roofs" cx="0.55" cy="0.45" r="0.4">
      <stop offset="0" stop-color="#d9b7a2" stop-opacity="0.6"/>
      <stop offset="1" stop-color="#d9b7a2" stop-opacity="0"/>
    </radialGradient>
    <radialGradient id="storm-debris" cx="0.7" cy="0.82" r="0.45">
      <stop offset="0" stop-color="#e0c59b" stop-opacity="0.7"/>
      <stop offset="1" stop-color="#e0c59b" stop-opacity="0"/>
    </radialGradient>
    <radialGradient id="storm-green" cx="0.45" cy="0.6" r="0.3">
      <stop offset="0" stop-color="#5f6b3a" stop-opacity="0.7"/>
      <stop offset="1" stop-color="#5f6b3a" stop-opacity="0"/>
    </radialGradient>
  </defs>
  <g role="img" aria-label="Photo: hillside town with homes and palms destroyed by a hurricane" clip-path="url(#clip-storm)">
    <rect x="440" y="0" width="856" height="272" fill="url(#storm-base)"/>
    <rect x="440" y="0" width="856" height="272" fill="url(#storm-green)"/>
    <rect x="440" y="0" width="856" height="272" fill="url(#storm-roofs)"/>
    <rect x="440" y="0" width="856" height="272" fill="url(#storm-house)"/>
    <rect x="440" y="0" width="856" height="272" fill="url(#storm-debris)"/>
  </g>
  <polygon class="panel" points="0,0 582,0 460,272 0,272"/>
  <polygon class="stripe" points="582,0 657,0 490,218 460,272"/>
  <rect class="logo-square" x="24" y="44" width="24" height="32"/>
  <text class="brand-name" x="48" y="78">Velmar Brook</text>
  <text class="brand-line" x="46" y="130">Claim Service, Inc</text>
  <text class="contact-head" x="54" y="174">Contact</text>
  <text class="contact-line" x="54" y="194">Gerald M. Hollis</text>
  <text class="contact-line" x="54" y="215">Email: ghollis@brindlevault.com</text>
  <text class="contact-line" x="54" y="235">Phone: (800) 555-0147, Ext. 2861</text>
  <text class="tagline" x="623" y="255" textLength="562" lengthAdjust="spacingAndGlyphs">Appraisal and Umpire Services</text>
</svg>

<svg class="banner banner--fire" viewBox="0 0 1296 272" xmlns="http://www.w3.org/2000/svg">
  <defs>
    <clipPath id="clip-fire"><polygon points="657,0 1296,0 1296,272 460,272"/></clipPath>
    <linearGradient id="fire-base" x1="0" y1="0" x2="1" y2="0">
      <stop offset="0" stop-color="#3e3d3c"/>
      <stop offset="0.35" stop-color="#5a5856"/>
      <stop offset="0.6" stop-color="#8c8f93"/>
      <stop offset="1" stop-color="#b7bcc2"/>
    </linearGradient>
    <linearGradient id="fire-ground" x1="0" y1="0" x2="0" y2="1">
      <stop offset="0.6" stop-color="#3a3634" stop-opacity="0"/>
      <stop offset="1" stop-color="#3a3634" stop-opacity="0.75"/>
    </linearGradient>
    <radialGradient id="fire-smoke" cx="0.6" cy="0.25" r="0.4">
      <stop offset="0" stop-color="#e6e9ec" stop-opacity="0.8"/>
      <stop offset="1" stop-color="#e6e9ec" stop-opacity="0"/>
    </radialGradient>
    <radialGradient id="fire-glow" cx="0.72" cy="0.62" r="0.12">
      <stop offset="0" stop-color="#ff7a1e" stop-opacity="0.75"/>
      <stop offset="1" stop-color="#ff7a1e" stop-opacity="0"/>
    </radialGradient>
    <radialGradient id="fire-walls" cx="0.3" cy="0.45" r="0.3">
      <stop offset="0" stop-color="#9d9990" stop-opacity="0.6"/>
      <stop offset="1" stop-color="#9d9990" stop-opacity="0"/>
    </radialGradient>
  </defs>
  <g role="img" aria-label="Photo: burned apartment building with smoke and small flames" clip-path="url(#clip-fire)">
    <rect x="440" y="0" width="856" height="272" fill="url(#fire-base)"/>
    <rect x="440" y="0" width="856" height="272" fill="url(#fire-walls)"/>
    <rect x="440" y="0" width="856" height="272" fill="url(#fire-smoke)"/>
    <rect x="440" y="0" width="856" height="272" fill="url(#fire-glow)"/>
    <rect x="440" y="0" width="856" height="272" fill="url(#fire-ground)"/>
  </g>
  <polygon class="panel" points="0,0 582,0 460,272 0,272"/>
  <polygon class="stripe" points="582,0 657,0 490,218 460,272"/>
  <rect class="logo-square" x="24" y="44" width="24" height="32"/>
  <text class="brand-name" x="48" y="78">Velmar Brook</text>
  <text class="brand-line" x="46" y="130">Claim Service, Inc</text>
  <text class="contact-head" x="54" y="174">Contact</text>
  <text class="contact-line" x="54" y="194">Gerald M. Hollis</text>
  <text class="contact-line" x="54" y="215">Email: ghollis@brindlevault.com</text>
  <text class="contact-line" x="54" y="235">Phone: (800) 555-0147, Ext. 2861</text>
  <text class="tagline" x="623" y="255" textLength="562" lengthAdjust="spacingAndGlyphs">Appraisal and Umpire Services</text>
</svg>

<svg class="banner banner--tornado" viewBox="0 0 1296 272" xmlns="http://www.w3.org/2000/svg">
  <defs>
    <clipPath id="clip-tornado"><polygon points="657,0 1296,0 1296,272 460,272"/></clipPath>
    <linearGradient id="tornado-base" x1="0" y1="0" x2="0" y2="1">
      <stop offset="0" stop-color="#d5dde6"/>
      <stop offset="0.2" stop-color="#a89c8c"/>
      <stop offset="0.45" stop-color="#c9c6c2"/>
      <stop offset="0.75" stop-color="#7f7a78"/>
      <stop offset="1" stop-color="#55504e"/>
    </linearGradient>
    <radialGradient id="tornado-wall" cx="0.5" cy="0.55" r="0.22">
      <stop offset="0" stop-color="#8c6a86" stop-opacity="0.65"/>
      <stop offset="1" stop-color="#8c6a86" stop-opacity="0"/>
    </radialGradient>
    <radialGradient id="tornado-roof" cx="0.62" cy="0.25" r="0.3">
      <stop offset="0" stop-color="#c8a478" stop-opacity="0.7"/>
      <stop offset="1" stop-color="#c8a478" stop-opacity="0"/>
    </radialGradient>
    <radialGradient id="tornado-siding" cx="0.88" cy="0.5" r="0.22">
      <stop offset="0" stop-color="#e8ecef" stop-opacity="0.8"/>
      <stop offset="1" stop-color="#e8ecef" stop-opacity="0"/>
    </radialGradient>
    <radialGradient id="tornado-tarp" cx="0.75" cy="0.75" r="0.2">
      <stop offset="0" stop-color="#3d4a5a" stop-opacity="0.6"/>
      <stop offset="1" stop-color="#3d4a5a" stop-opacity="0"/>
    </radialGradient>
  </defs>
  <g role="img" aria-label="Photo: house with roof torn off and debris after a tornado" clip-path="url(#clip-tornado)">
    <rect x="440" y="0" width="856" height="272" fill="url(#tornado-base)"/>
    <rect x="440" y="0" width="856" height="272" fill="url(#tornado-siding)"/>
    <rect x="440" y="0" width="856" height="272" fill="url(#tornado-roof)"/>
    <rect x="440" y="0" width="856" height="272" fill="url(#tornado-wall)"/>
    <rect x="440" y="0" width="856" height="272" fill="url(#tornado-tarp)"/>
  </g>
  <polygon class="panel" points="0,0 582,0 460,272 0,272"/>
  <polygon class="stripe" points="582,0 657,0 490,218 460,272"/>
  <rect class="logo-square" x="24" y="44" width="24" height="32"/>
  <text class="brand-name" x="48" y="78">Velmar Brook</text>
  <text class="brand-line" x="46" y="130">Claim Service, Inc</text>
  <text class="contact-head" x="54" y="174">Contact</text>
  <text class="contact-line" x="54" y="194">Gerald M. Hollis</text>
  <text class="contact-line" x="54" y="215">Email: ghollis@brindlevault.com</text>
  <text class="contact-line" x="54" y="235">Phone: (800) 555-0147, Ext. 2861</text>
  <text class="tagline" x="623" y="255" textLength="562" lengthAdjust="spacingAndGlyphs">Appraisal and Umpire Services</text>
</svg>

</body>
</html>
```